依頼詳細
ラベルのデザインを募集します。

基本的には、幅91.5mm 縦131mmの縦長で角が少し丸いシールにいれるデザインです
・データは様々な形で使用させて頂きます。
(ホームページに載せたり、サンプル品に使用するなど)

クラフトのチャック袋(スタンドパック)にラベルを貼る予定です。
■キャッチフレーズなど
・魔法のスーパーフード タイガーナッツ!パウダータイプ

記載項目
商品名:星屑のコモレビパウダー
その他キャッチフレーズ、キーワードなど:スーパーフード
希望イメージ
シンプル 複雑
単色 カラフル
暗い 明るい
日常 高級
遊び心 厳粛
未来的 伝統的
女性的 男性的
希望する色
赤系、黄・オレンジ系
納品ファイル
• イラストレーター形式 (.ai)
• フォトショップ形式 (.psd)
補足説明
送付ファイルはパウダーの写真です。特に使わなくても大丈夫ですが、色合いなど確認するのにお使いください。
粒状態の画像を追加します。
製品自体は粉なので参考にしてください。
使わなくても大丈夫です。
■ 選んだ理由

自分の考えていたイメージに近く、魔法感がよく出ていて
まとまっていたのでこちらを選ばせて頂きました。

■ 提案者全員のお礼・コメント

多数のご応募ありがとうございました。
またの機会がありましたら、よろしくお願い足します。

```html
<!DOCTYPE html>
<html lang="ja">
<head>
<meta charset="utf-8">
<title>星屑のコモレビパウダー ラベル</title>
<link href="https://fonts.googleapis.com/css2?family=Great+Vibes&family=Noto+Sans+JP:wght@500;700&family=Shippori+Mincho+B1:wght@800&display=swap" rel="stylesheet">
<style>
  :root {
    --page: #ffffff;
    --orange: #d9731f;
    --orange-light: #e5893a;
    --cream: #fbf1df;
    --brown: #3a2014;
    --script: #d0701f;
    --white: #ffffff;
    --red: #d8453a;
    --green: #6a9a3a;
    --amber: #e08a1e;
    --leaf: #4f9a5a;
  }
  html, body {
    margin: 0;
    width: 841px;
    height: 1200px;
    overflow: hidden;
    background: var(--page);
  }
  .label {
    position: absolute;
    left: 154px;
    top: 224px;
    width: 533px;
    height: 743px;
    border-radius: 22px;
    background: var(--orange);
    overflow: hidden;
  }
  .ornament-band {
    position: absolute;
    left: 0;
    width: 100%;
    background: linear-gradient(var(--orange-light), var(--orange));
  }
  .ornament-band.top { top: 0; height: 78px; }
  .ornament-band.bottom { bottom: 0; height: 112px; background: linear-gradient(var(--orange), var(--orange-light)); }
  .title-panel {
    position: absolute;
    left: 42px;
    top: 78px;
    width: 449px;
    height: 400px;
    background: var(--cream);
    border-radius: 14px;
  }
  .subtitle-script {
    position: absolute;
    left: 84px;
    top: 144px;
    margin: 0;
    font-family: "Great Vibes", cursive;
    font-size: 34px;
    color: var(--script);
  }
  .product-name {
    position: absolute;
    left: 0;
    top: 232px;
    width: 100%;
    margin: 0;
    text-align: center;
    font-family: "Shippori Mincho B1", serif;
    font-weight: 800;
    font-size: 50px;
    line-height: 62px;
    color: var(--brown);
  }
  .sparkle {
    position: absolute;
    left: 342px;
    top: 222px;
  }
  .description {
    position: absolute;
    left: 0;
    top: 496px;
    width: 100%;
    margin: 0;
    text-align: center;
    font-family: "Noto Sans JP", sans-serif;
    font-weight: 500;
    font-size: 16px;
    line-height: 30px;
    color: var(--white);
  }
  .nutrients {
    position: absolute;
    left: 92px;
    top: 558px;
    display: flex;
    gap: 18px;
    margin: 0;
    padding: 0;
    list-style: none;
  }
  .nutrient {
    width: 64px;
    height: 64px;
    border-radius: 50%;
    background: var(--white);
    display: flex;
    align-items: center;
    justify-content: center;
    font-family: "Noto Sans JP", sans-serif;
    font-weight: 700;
    font-size: 11px;
    white-space: nowrap;
  }
  .nutrient.vitamin { color: var(--red); }
  .nutrient.mineral { color: var(--green); }
  .nutrient.oleic { color: var(--amber); }
  .nutrient.fiber { color: var(--leaf); }
</style>
</head>
<body>
  <div class="label">
    <div class="ornament-band top" role="img" aria-label="アーチ模様の装飾帯"></div>
    <div class="ornament-band bottom" role="img" aria-label="アーチ模様の装飾帯"></div>
    <div class="title-panel"></div>
    <p class="subtitle-script">Komorebi Powder</p>
    <h1 class="product-name">星屑の<br>コモレビ<br>パウダー</h1>
    <svg class="sparkle" width="40" height="40" viewBox="0 0 40 40" aria-hidden="true">
      <path d="M20 0 L23 17 L40 20 L23 23 L20 40 L17 23 L0 20 L17 17 Z" fill="#3a2014"/>
    </svg>
    <p class="description">豊富な栄養素で注目のスーパーフード。<br>グルテンを含まず、小麦粉の代用にも最適です。</p>
    <ul class="nutrients">
      <li class="nutrient vitamin">ビタミンE</li>
      <li class="nutrient mineral">ミネラル</li>
      <li class="nutrient oleic">オレイン酸</li>
      <li class="nutrient fiber">食物繊維</li>
    </ul>
  </div>
</body>
</html>
```